Flyer-Design für Weihnachtsbäume als Dekoration
Zielgruppe
Wir bearbeiten Bleche nach Kundenvorgaben. Nebenbei stellen wir immer mal ein paar Dekoartikel
bzw. Sonderanfertigen her.
https://feinblechwerk-muster.de/
http://www.talbergwerk.de/
https://feinblechwerk-muster.de/aktuelles/image-broschuere/
Mit diesem Flyer wollen wir für unsere Weihnachtsbäume werben. Die Preise sind Endpreis inkl. Mehrwertsteuer.
Aufgabenstellung
Ich hab noch mehr Bildmaterial zur Verfügung.

```html
<!DOCTYPE html>
<html lang="de">
<head>
<meta charset="utf-8">
<title>Weihnachtsbäume – Varianten</title>
<link href="https://fonts.googleapis.com/css2?family=Kaushan+Script&family=Lato:wght@300;400&family=Oswald:wght@500;600&display=swap" rel="stylesheet">
<style>
  :root {
    --page-bg: #e9e9e9;
    --paper: #f8f8f9;
    --gold-dark: #b8924f;
    --gold-panel: #d3c189;
    --gold-soft: #dccd9c;
    --gold-text: #c9ab4f;
    --white: #ffffff;
    --speckle: #e3e3e6;
  }
  html, body {
    margin: 0;
    width: 1200px;
    height: 800px;
    overflow: hidden;
    background: var(--page-bg);
  }
  .flyer {
    position: absolute;
    left: 250px;
    top: 50px;
    width: 700px;
    height: 700px;
    background: var(--paper);
    box-shadow: 0 12px 40px rgba(0,0,0,0.12);
    overflow: hidden;
  }
  .frame-top {
    position: absolute; left: 0; top: 0; width: 700px; height: 14px;
    background: var(--gold-dark);
  }
  .frame-right {
    position: absolute; right: 0; top: 0; width: 18px; height: 700px;
    background: var(--gold-dark);
  }
  .gold-panel {
    position: absolute; left: 0; top: 14px; width: 590px; height: 560px;
    background: var(--gold-panel);
  }
  .product-photo {
    position: absolute; left: 590px; top: 14px; width: 92px; height: 450px;
    background: linear-gradient(180deg, #dedddb 0%, #cfc9c2 40%, #8f7e6c 70%, #2e2c2c 100%);
  }
  .tree-drawing {
    position: absolute; left: 40px; top: 440px; width: 540px; height: 120px;
    background: radial-gradient(ellipse at 25% 60%, var(--gold-soft) 0%, var(--gold-panel) 70%);
  }
  .speckle-area {
    position: absolute; left: 0; top: 574px; width: 682px; height: 126px;
    background: linear-gradient(180deg, var(--paper) 0%, var(--speckle) 100%);
  }
  .variants {
    position: absolute; left: 60px; top: 95px; width: 500px;
    color: var(--white);
  }
  .variants__title {
    font-family: "Kaushan Script", cursive;
    font-weight: 400;
    font-size: 36px;
    margin: 0 0 16px;
  }
  .variant-list { list-style: none; margin: 0; padding: 0; }
  .variant {
    display: grid;
    grid-template-columns: 1fr 100px 90px;
    align-items: end;
    height: 44px;
    border-bottom: 1px solid var(--white);
    font-family: "Lato", sans-serif;
    font-weight: 300;
    font-size: 12px;
    letter-spacing: 0.2px;
    padding-bottom: 5px;
    box-sizing: border-box;
  }
  .variant__height { font-size: 11px; }
  .variant__price {
    font-family: "Oswald", sans-serif;
    font-weight: 600;
    font-size: 17px;
    text-align: right;
    align-self: start;
    padding-top: 4px;
  }
  .web-badge {
    position: absolute; left: 215px; top: 600px; width: 270px; height: 44px;
    border: 2px solid var(--gold-text);
    box-sizing: border-box;
    display: flex; align-items: center; justify-content: center;
    font-family: "Oswald", sans-serif;
    font-weight: 500;
    font-size: 19px;
    letter-spacing: 0.5px;
    color: var(--gold-text);
  }
</style>
</head>
<body>
  <article class="flyer">
    <div class="gold-panel" role="img" aria-label="Goldfarben getönter Hintergrund mit Weihnachtskugeln an einem Blechbaum"></div>
    <div class="product-photo" role="img" aria-label="Foto eines dekorierten Weihnachtsbaums aus Blech mit Sternen"></div>
    <div class="tree-drawing" role="img" aria-label="Weiße Strichzeichnung eines Tannenbaums mit auslaufender geschwungener Linie"></div>
    <div class="speckle-area" role="img" aria-label="Heller Hintergrund mit feinen grauen Farbspritzern"></div>

    <section class="variants">
      <h2 class="variants__title">Varianten</h2>
      <ul class="variant-list">
        <li class="variant"><span class="variant__name">Weihnachtsbaum mit Platz für 7 Weihnachtskugeln</span><span class="variant__height">Höhe: 50cm</span><span class="variant__price">54,99 €</span></li>
        <li class="variant"><span class="variant__name">Weihnachtsbaum mit Platz für 13 Weihnachtskugeln</span><span class="variant__height">Höhe: 80cm</span><span class="variant__price">124,99 €</span></li>
        <li class="variant"><span class="variant__name">Weihnachtsbaum mit Platz für 13 Weihnachtskugeln</span><span class="variant__height">Höhe: 110cm</span><span class="variant__price">154,99 €</span></li>
        <li class="variant"><span class="variant__name">Weihnachtsbaum mit Platz für 13 Weihnachtskugeln</span><span class="variant__height">Höhe: 140cm</span><span class="variant__price">184,99 €</span></li>
        <li class="variant"><span class="variant__name">Weihnachtsbaum mit Platz für 13 Weihnachtskugeln</span><span class="variant__height">Höhe: 170cm</span><span class="variant__price">214,99 €</span></li>
      </ul>
    </section>

    <div class="web-badge">FEINBLECHWERK-MUSTER.DE</div>

    <div class="frame-top"></div>
    <div class="frame-right"></div>
  </article>
</body>
</html>
```